Marlow Estate Group (Real Estate and Investment)

A high end, clean design.
We are a real estate company with sales, asset management and investment divisions. We want to use a black and white scheme which is really high end feel. The back of the card can just be the logo (black background with the white writing) as we will probably emboss this when we print)

Target Market(s)

High level investors, high end houses for sale

Industry/Entity Type

Business

Contact Information for Business Card

Name, position, phone number and email address
Ben Marlow, Managing Director, 0438926057 and ben@marlowestate.com.au

Requirements
Must have
• Back of the card to be the black background with the white writing (as per the attached images). Would like the capacity to emboss the writing and logo

```html
<!DOCTYPE html>
<html lang="en">
<head>
<meta charset="utf-8">
<title>Marlow Estate Group – Business Card</title>
<link href="https://fonts.googleapis.com/css2?family=Roboto:wght@300;400;700&display=swap" rel="stylesheet">
<style>
  :root {
    --ink: #0b0b0b;
    --paper: #ffffff;
    --stage: #5d6469;
    --muted: #cfcfcf;
  }
  * { margin: 0; padding: 0; box-sizing: border-box; }
  html, body { width: 1200px; height: 900px; overflow: hidden; }
  body {
    background: var(--stage);
    font-family: "Roboto", Arial, sans-serif;
    position: relative;
  }
  .card {
    position: absolute;
    width: 560px;
    height: 320px;
    border-radius: 22px;
    overflow: hidden;
    background: var(--ink);
  }
  .card--front { left: 560px; top: 100px; }
  .card--back  { left: 80px;  top: 480px; }

  .card__shape { position: absolute; inset: 0; }

  .contact {
    position: absolute;
    left: 40px;
    top: 42px;
    color: var(--paper);
  }
  .contact__name { font-size: 22px; font-weight: 700; letter-spacing: 0.2px; }
  .contact__role { font-size: 11px; font-weight: 300; color: var(--muted); margin-top: 3px; }
  .contact__list { list-style: none; margin-top: 24px; }
  .contact__item {
    display: flex; align-items: center; gap: 10px;
    font-size: 13px; font-weight: 300; margin-bottom: 9px;
  }
  .contact__icon { width: 13px; height: 13px; fill: var(--paper); flex: none; }

  .brand {
    position: absolute;
    display: flex;
    align-items: center;
    gap: 14px;
  }
  .brand__dot {
    width: 34px; height: 34px; border-radius: 50%;
    border: 2px solid currentColor;
    flex: none;
  }
  .brand__name {
    font-size: 24px;
    font-weight: 300;
    letter-spacing: 1.5px;
    text-transform: uppercase;
    line-height: 1.15;
  }
  .brand--front { right: 36px; top: 130px; color: var(--ink); }
  .brand--back  { left: 50%; top: 50%; transform: translate(-50%, -50%); color: var(--paper); }
  .brand--back .brand__name { font-size: 30px; }
  .brand--back .brand__dot { width: 44px; height: 44px; }
</style>
</head>
<body>

  <section class="card card--front" aria-label="Business card front">
    <svg class="card__shape" viewBox="0 0 560 320" aria-hidden="true">
      <path d="M300 0 Q228 150 248 320 H560 V0 Z" fill="var(--paper)"/>
      <path d="M280 0 Q206 150 226 320" fill="none" stroke="var(--paper)" stroke-width="5"/>
    </svg>

    <div class="contact">
      <p class="contact__name">Ben Marlow</p>
      <p class="contact__role">Managing Director</p>
      <ul class="contact__list">
        <li class="contact__item">
          <svg class="contact__icon" viewBox="0 0 24 24" aria-hidden="true"><path d="M6.6 10.8a15.1 15.1 0 0 0 6.6 6.6l2.2-2.2a1 1 0 0 1 1-.25 11.4 11.4 0 0 0 3.6.57 1 1 0 0 1 1 1V20a1 1 0 0 1-1 1A17 17 0 0 1 3 4a1 1 0 0 1 1-1h3.5a1 1 0 0 1 1 1c0 1.25.2 2.45.57 3.57a1 1 0 0 1-.25 1z"/></svg>
          0438926057
        </li>
        <li class="contact__item">
          <svg class="contact__icon" viewBox="0 0 24 24" aria-hidden="true"><path d="M2 5h20v14H2z M4 7v.5l8 5 8-5V7l-8 5z" fill-rule="evenodd"/></svg>
          ben@marlowestate.com.au
        </li>
      </ul>
    </div>

    <div class="brand brand--front">
      <span class="brand__dot" aria-hidden="true"></span>
      <span class="brand__name">Marlow Estate<br>Group</span>
    </div>
  </section>

  <section class="card card--back" aria-label="Business card back">
    <div class="brand brand--back">
      <span class="brand__dot" aria-hidden="true"></span>
      <span class="brand__name">Marlow Estate Group</span>
    </div>
  </section>

</body>
</html>
```